I need a website built for my organization.
We are the world's largest network of music producers.
The website should be professional, sharp, and high quality., We need a website built for The Halvern Sound Guild. We are one of the World's largest association of music producers.
The site must be professional, sharp, and high quality., I need a website built for my organization.
The site must be professional, sharp, and high quality.
Somewhere in the top half of the site there should be a form for the user to fill out. The details of the form are as follows:
Title (large and bold): Contact Us or Submit Your Music
Fields to include (* = required): First Name*, Last Name*, Age, Zip Code, Email Address*, Daytime Phone, Evening Phone, Comments
Then, there will be a "submit" button to proceed to next step of form. Just below the "submit" button, should be the following verbiage: "After submitting, you will have the opportunity to upload demos of your music (optional) and provide other pertinent information about yourself, band, or group."
Target Market(s)
Music producers and aspiring musicians
Industry/Entity Type
Group
Colors
Designer to choose colors to be used in the design.
Look and feel

```html
<!DOCTYPE html>
<html lang="en">
<head>
<meta charset="utf-8">
<title>The Halvern Sound Guild</title>
<link href="https://fonts.googleapis.com/css2?family=Oswald:wght@700&family=Open+Sans:wght@400;600;700&family=Roboto+Condensed:wght@400&display=swap" rel="stylesheet">
<style>
:root{
  --page:#ffffff;
  --header:#cacaca;
  --ink:#3f3f3f;
  --tab:#e9e9e9;
  --tab-active:#3b3b3b;
  --hero-dark:#050505;
  --hero-mid:#3a3a3a;
  --panel:#d6d6d6;
  --field:#ffffff;
  --field-text:#9a9a9a;
  --required:#d42020;
  --submit-top:#1f8cff;
  --submit-bottom:#0033c4;
  --bar:#bfbfbf;
  --track-bg:#ebebeb;
  --progress:#5fb85f;
  --social:#5a5a5a;
}
*{box-sizing:border-box;margin:0;padding:0}
html,body{width:1133px;height:1200px;overflow:hidden;background:var(--page)}
body{position:relative;font-family:"Open Sans",sans-serif}
.abs{position:absolute}
.site-header{left:23px;top:44px;width:1087px;height:123px;background:linear-gradient(#b8b8b8 0,#d0d0d0 4px,#c6c6c6 100%);border-bottom:2px solid #9a9a9a}
.brand{left:37px;top:10px;width:460px;text-align:center;font-family:"Oswald",sans-serif;font-weight:700;font-size:47px;line-height:50px;color:var(--ink);letter-spacing:-.5px}
.main-nav{left:510px;top:87px;display:flex;gap:1px}
.main-nav a{display:block;width:124px;height:38px;line-height:38px;text-align:center;font-size:19px;color:#444;text-decoration:none;background:linear-gradient(#f2f2f2,#dcdcdc);border:1px solid #8a8a8a;border-bottom:none;border-radius:8px 8px 0 0}
.main-nav a.active{background:linear-gradient(#5a5a5a,#2a2a2a);color:#fff}
.hero{left:23px;top:167px;width:1087px;height:611px;background:radial-gradient(circle at 195px 220px,#8c8c8c 0,#555 60px,#262626 150px,transparent 260px),radial-gradient(ellipse at 210px 480px,#2a2a2a 0,transparent 200px),linear-gradient(90deg,var(--hero-mid),var(--hero-dark) 55%,#101010)}
.form-card{left:545px;top:249px;width:479px;height:454px;background:var(--panel);border-radius:12px;box-shadow:inset 0 0 20px rgba(255,255,255,.6)}
.tab{font-size:17px;color:#222}
.tab-active{left:568px;top:286px;width:168px;height:32px;line-height:32px;text-align:center;background:linear-gradient(#6a6664,#3a3836);color:#fff;border-radius:6px 6px 0 0}
.tab-plain{left:757px;top:292px}
.form-box{left:568px;top:317px;width:433px;height:192px;background:linear-gradient(#7b7775,#2c2b2b);border:1px solid #555}
.field{background:var(--field);border-radius:3px;font-size:10.5px;color:var(--field-text);padding-left:6px;display:flex;align-items:center;box-shadow:inset 0 1px 2px rgba(0,0,0,.25)}
.star{color:var(--required);font-size:11px}
.req-note{left:603px;top:323px;font-size:7px;color:var(--required)}
.mini-label{font-size:8px;color:#fff;font-weight:600}
.submit-btn{left:712px;top:558px;width:155px;height:41px;border-radius:5px;background:linear-gradient(var(--submit-top),var(--submit-bottom));border:1px solid #0a2a80;color:#fff;font-weight:700;font-size:19px;letter-spacing:1.5px;text-align:center;line-height:39px}
.submit-note{left:590px;top:607px;width:390px;text-align:center;font-family:"Roboto Condensed",sans-serif;font-size:10.5px;line-height:18px;color:#333;letter-spacing:-.4px}
.player-bar{left:23px;top:778px;width:1087px;height:147px;background:var(--bar)}
.track{left:371px;top:811px;width:243px;height:83px;background:var(--track-bg);border-radius:2px}
.track-title{left:16px;top:27px;font-size:15px;color:#555}
.track-time{right:16px;top:26px;font-size:16px;font-weight:600;color:#555}
.progress{left:16px;top:53px;width:211px;height:8px;border:1px solid #555;background:#fff}
.progress span{display:block;width:58%;height:100%;background:var(--progress)}
.social{width:56px;height:56px;border-radius:50%;background:var(--social);color:#fff;font-size:9px;font-weight:600;display:flex;align-items:center;justify-content:center}
.site-footer{left:23px;top:925px;width:1087px;height:78px;background:radial-gradient(ellipse at 260px 0,#3a3a3a 0,transparent 220px),#060606;color:#fff;font-size:13px;text-align:center;line-height:88px}
</style>
</head>
<body>
<header class="site-header abs">
  <div class="brand abs">The Halvern Sound<br>Guild</div>
  <nav class="main-nav abs">
    <a class="active" href="#">HOME</a><a href="#">ABOUT US</a><a href="#">MEMBERS</a><a href="#">ARCHIVE</a>
  </nav>
</header>

<div class="hero abs" role="img" aria-label="Black and white photo of a stage microphone on a stand against a dark background"></div>

<section class="form-card abs" aria-label="Submission form"></section>
<div class="tab tab-active abs">Submit Your Music</div>
<div class="tab tab-plain abs">Contact Us</div>
<div class="form-box abs"></div>
<span class="star abs" style="left:603px;top:316px">*</span>
<span class="req-note abs">required</span>

<span class="star abs" style="left:603px;top:358px">*</span>
<div class="field abs" style="left:613px;top:355px;width:156px;height:27px">First Name</div>
<span class="star abs" style="left:793px;top:358px">*</span>
<div class="field abs" style="left:803px;top:355px;width:156px;height:27px">Last Name</div>
<span class="star abs" style="left:603px;top:398px">*</span>
<div class="field abs" style="left:613px;top:396px;width:156px;height:27px">Email Address</div>
<div class="field abs" style="left:613px;top:442px;width:47px;height:23px;padding-left:8px">Age</div>
<div class="field abs" style="left:698px;top:442px;width:71px;height:23px;padding-left:12px">Zip Code</div>

<span class="mini-label abs" style="left:847px;top:392px">Daytime phone</span>
<div class="field abs" style="left:803px;top:403px;width:34px;height:20px"></div>
<div class="field abs" style="left:848px;top:403px;width:111px;height:20px"></div>
<span class="mini-label abs" style="left:847px;top:433px">Evening phone</span>
<div class="field abs" style="left:803px;top:445px;width:34px;height:20px"></div>
<div class="field abs" style="left:848px;top:445px;width:111px;height:20px"></div>

<div class="submit-btn abs">SUBMIT</div>
<p class="submit-note abs">After submitting, you will have the opportunity to upload demos of your music (optional) and<br>provide other pertinent information about yourself, band, or group.</p>

<section class="player-bar abs"></section>
<svg class="abs" style="left:40px;top:800px" width="260" height="100" viewBox="0 0 260 100">
  <defs><linearGradient id="btn" x1="0" y1="0" x2="0" y2="1"><stop offset="0" stop-color="#e4e4e4"/><stop offset="1" stop-color="#b0b0b0"/></linearGradient></defs>
  <circle cx="43" cy="51" r="28" fill="url(#btn)" stroke="#8e8e8e" stroke-width="2"/>
  <rect x="29" y="42" width="28" height="18" rx="3" fill="#555"/>
  <path d="M43 45 L35 51 L43 57 Z M51 45 L43 51 L51 57 Z" fill="#ddd"/>
  <circle cx="127" cy="51" r="40" fill="url(#btn)" stroke="#f2f2f2" stroke-width="3"/>
  <rect x="110" y="34" width="34" height="34" rx="5" fill="#555"/>
  <path d="M121 42 L136 51 L121 60 Z" fill="#ddd"/>
  <circle cx="214" cy="51" r="28" fill="url(#btn)" stroke="#8e8e8e" stroke-width="2"/>
  <rect x="200" y="42" width="28" height="18" rx="3" fill="#555"/>
  <path d="M206 45 L214 51 L206 57 Z M214 45 L222 51 L214 57 Z" fill="#ddd"/>
</svg>
<div class="track abs">
  <span class="track-title abs">Night Circuit</span>
  <span class="track-time abs">2:05</span>
  <div class="progress abs"><span></span></div>
</div>
<div class="social abs" style="left:772px;top:824px">Linkup</div>
<div class="social abs" style="left:857px;top:824px">Chirper</div>
<div class="social abs" style="left:943px;top:824px">Vidstream</div>
<div class="social abs" style="left:1024px;top:824px">Feed</div>

<footer class="site-footer abs">© 2013 Halvern Sound Guild &nbsp;|&nbsp; All Rights Reserved</footer>
</body>
</html>
```